COMPANY SIGN

I am in the process of ordering new company For Sale signs and stationary (business cards, envelopes, letterheads, and labels). I need a new design with my existing company logo. The TWO MOST IMPORTANT PROJECTS I need right now is the new design for the company sign and business cards. I've uploaded a .jpg file of my company logo.

I like the design to be eye catching and the background color of the company sign to be soothing to the eyes. Perhaps, using one of the color on the leaves of the logo or any other color that the designer think will go well with the logo. My favorite colors are teal or light olive color but don't let that affect your creativity.

Industry/Entity Type

Business

Requirements
Should not have
• Please don't use "Times New Roman" fonts or fonts that is hard to read.

```html
<!DOCTYPE html>
<html lang="en">
<head>
<meta charset="utf-8">
<title>Maplewood Open House – Company Sign</title>
<link rel="stylesheet" href="https://fonts.googleapis.com/css2?family=Questrial&display=swap">
<style>
  :root {
    --page-bg: #ebebeb;
    --sign-fill: #aec57a;
    --sign-rim: #82ad5c;
    --ink: #5a4630;
    --ink-soft: #6e5d42;
    --hole: #ffffff;
  }
  html, body {
    margin: 0;
    padding: 0;
    width: 800px;
    height: 1200px;
    overflow: hidden;
    background: var(--page-bg);
  }
  .canvas {
    position: relative;
    width: 800px;
    height: 1200px;
    display: flex;
    align-items: center;
    justify-content: center;
  }
  .company-sign {
    width: 600px;
    height: auto;
    display: block;
  }
  .sign-body {
    fill: var(--sign-fill);
    stroke: var(--sign-rim);
    stroke-width: 10;
  }
  .mount-hole {
    fill: var(--hole);
    stroke: var(--sign-rim);
    stroke-width: 2.5;
  }
  .sign-text {
    font-family: "Questrial", "Century Gothic", sans-serif;
    text-anchor: middle;
  }
  .web-address { fill: var(--ink-soft); font-size: 13px; }
  .brand-name { fill: var(--ink); font-size: 40px; }
  .brand-dot { fill: var(--ink); }
  .contact-name { fill: var(--ink); font-size: 20px; letter-spacing: 0.5px; }
  .contact-phone { fill: var(--ink-soft); font-size: 17px; letter-spacing: 0.5px; }
</style>
</head>
<body>
  <main class="canvas">
    <svg class="company-sign" viewBox="-6 -6 472 406" xmlns="http://www.w3.org/2000/svg" role="group" aria-label="Maplewood Open House yard sign">
      <path class="sign-body" d="M53,0 H407 Q427,0 427,20 V70 C455,110 460,150 460,197 C460,244 455,284 427,324 V374 Q427,394 407,394 H53 Q33,394 33,374 V324 C5,284 0,244 0,197 C0,150 5,110 33,70 V20 Q33,0 53,0 Z"/>

      <circle class="mount-hole" cx="65" cy="32" r="5"/>
      <circle class="mount-hole" cx="395" cy="32" r="5"/>
      <circle class="mount-hole" cx="65" cy="362" r="5"/>
      <circle class="mount-hole" cx="395" cy="362" r="5"/>

      <text class="sign-text web-address" x="230" y="37">www.webaddress.com</text>

      <circle class="brand-dot" cx="230" cy="118" r="14"/>
      <text class="sign-text brand-name" x="230" y="195">Maplewood</text>
      <text class="sign-text brand-name" x="230" y="240">Open House</text>

      <text class="sign-text contact-name" x="230" y="331">CONTACT NAME</text>
      <text class="sign-text contact-phone" x="230" y="366">TEL 000.000.0000</text>
    </svg>
  </main>
</body>
</html>
```